Bold Stragglers At Dusk Podcast Design

My audio drama podcast is a funny horror story with romantic elements called Bold Stragglers At Dusk.
I'm looking for a colorful design featuring the title and letting the viewer know this is a horror show.
The title needs to be clearly visible even in thumbnail size.

```html
<!DOCTYPE html>
<html lang="en">
<head>
<meta charset="utf-8">
<title>Bold Stragglers At Dusk — Podcast Cover</title>
<link rel="stylesheet" href="https://fonts.googleapis.com/css2?family=Rubik+Distressed&display=swap">
<style>
  :root {
    --backdrop: #2a2a2a;
    --blood: #d00a0a;
    --blood-deep: #8c0000;
    --night: #0b0000;
    --silhouette: #120000;
    --bone: #ffffff;
    --shadow-red: #7a0000;
  }
  * { margin: 0; padding: 0; box-sizing: border-box; }
  html, body {
    width: 1200px;
    height: 904px;
    overflow: hidden;
    background: var(--backdrop);
  }
  .cover {
    position: absolute;
    left: 170px;
    top: 22px;
    width: 860px;
    height: 860px;
    overflow: hidden;
    background:
      radial-gradient(ellipse 62% 58% at 55% 50%, var(--blood) 0%, var(--blood-deep) 62%, var(--night) 100%);
  }
  .cover__branches {
    position: absolute;
    left: 0;
    top: 0;
    width: 860px;
    height: 300px;
    background: linear-gradient(180deg, rgba(11,0,0,0.55) 0%, rgba(11,0,0,0) 100%);
  }
  .cover__graveyard {
    position: absolute;
    left: 0;
    bottom: 0;
    width: 860px;
    height: 420px;
  }
  .cover__frame {
    position: absolute;
    left: 38px;
    top: 38px;
    right: 38px;
    bottom: 38px;
    border: 1.5px solid var(--bone);
    pointer-events: none;
  }
  .cover__title {
    position: absolute;
    left: 60px;
    top: 62px;
    width: 740px;
    text-align: center;
    font-family: "Rubik Distressed", "Impact", sans-serif;
    font-weight: 400;
    color: var(--bone);
    text-transform: uppercase;
    line-height: 1;
    text-shadow: 4px 4px 0 var(--shadow-red), 6px 6px 4px rgba(0,0,0,0.45);
  }
  .cover__line { display: block; white-space: nowrap; }
  .cover__line--top { font-size: 78px; letter-spacing: 3px; }
  .cover__line--main { font-size: 100px; letter-spacing: -3px; margin-top: 22px; }
  .cover__line--bottom { font-size: 78px; letter-spacing: 3px; margin-top: 22px; }
  .initial { font-size: 1.25em; }
</style>
</head>
<body>
  <main class="cover">
    <div class="cover__branches" role="img" aria-label="Bare dark tree branches hanging from the top edge"></div>

    <svg class="cover__graveyard" viewBox="0 0 860 420" role="img" aria-label="Black silhouette of a haunted house with lit red windows and a graveyard of crosses and tombstones">
      <defs>
        <linearGradient id="houseFade" x1="0" y1="0" x2="0" y2="1">
          <stop offset="0" stop-color="#120000" stop-opacity="0.55"/>
          <stop offset="0.4" stop-color="#120000" stop-opacity="0.9"/>
          <stop offset="1" stop-color="#120000" stop-opacity="1"/>
        </linearGradient>
        <linearGradient id="groundFade" x1="0" y1="0" x2="0" y2="1">
          <stop offset="0" stop-color="#120000" stop-opacity="0.6"/>
          <stop offset="1" stop-color="#0b0000" stop-opacity="1"/>
        </linearGradient>
      </defs>
      <rect class="graveyard__house" x="68" y="30" width="290" height="390" rx="6" fill="url(#houseFade)"/>
      <rect class="graveyard__ground" x="0" y="330" width="860" height="90" fill="url(#groundFade)"/>
    </svg>

    <h1 class="cover__title">
      <span class="cover__line cover__line--top"><span class="initial">B</span>old</span>
      <span class="cover__line cover__line--main"><span class="initial">S</span>tragglers</span>
      <span class="cover__line cover__line--bottom"><span class="initial">A</span>t <span class="initial">D</span>usk</span>
    </h1>

    <div class="cover__frame"></div>
  </main>
</body>
</html>
```